Domestic Cleaning services needs a website

We need a descriptive, easy to use and trust inspiring website for domestic cleaning clients. It should be easy to use, with appointment scheduling and SMS notifiers. The brand name "BrightNest by Marguerite" should be associated with all offers at the website. blue/green/white colors should be more pronounced.
Website should be Mobile friendly.

Target Market(s)

Domestic Market. Long rental tourists, expats, local housewifes

Logo Text

BRIGHTNEST by MARGUERITE

Number of Pages Required

2 page

Font styles to use
Sans Serif

```html
<!DOCTYPE html>
<html lang="en">
<head>
<meta charset="utf-8">
<title>BrightNest by Marguerite – Our Services</title>
<link href="https://fonts.googleapis.com/css2?family=Montserrat:wght@300;400;500;600;700&display=swap" rel="stylesheet">
<style>
:root{
  --blue:#1560c8;
  --green:#14963a;
  --red:#e0452f;
  --text:#333;
  --muted:#666;
  --line:#dcdcdc;
  --footer-band:#e4e4e4;
  --white:#fff;
}
*{margin:0;padding:0;box-sizing:border-box}
html,body{width:1200px;height:2422px;overflow:hidden;background:var(--white)}
body{position:relative;font-family:"Montserrat",Arial,sans-serif;color:var(--text)}
.abs{position:absolute}

/* header */
.brand{left:202px;top:28px;display:flex;align-items:center;gap:10px;color:var(--blue);font-weight:500}
.brand-mark{width:22px;height:26px;background:var(--green)}
.brand-name{font-size:29px;line-height:1}
.brand-sub{font-size:12px;display:block;margin-top:2px}
.main-nav{left:492px;top:34px;display:flex;gap:8px}
.main-nav a{display:block;height:26px;line-height:26px;text-align:center;color:var(--white);background:var(--blue);font-size:13px;text-decoration:none;border-radius:2px}
.main-nav a.active{background:var(--green)}
.header-call{left:492px;top:68px;font-size:10px;font-weight:600;white-space:nowrap}
.header-call span{color:var(--green)}
.notify{left:972px;top:32px}
.header-rule{left:0;top:91px;width:1200px;height:1px;background:var(--line)}
.breadcrumb{left:202px;top:105px;font-size:8px;color:var(--muted)}

/* hero */
.hero{left:202px;top:130px;width:797px;height:206px;background:linear-gradient(100deg,#3a2414 0%,#8a4e22 35%,#c98a3e 60%,#6f3e18 100%)}
.section-title{left:0;top:392px;width:1200px;text-align:center;font-size:25px;font-weight:400;letter-spacing:.5px}

/* services */
.service{left:202px;width:797px;height:215px}
.service-photo{position:absolute;top:0;width:319px;height:215px}
.service.photo-left .service-photo{left:0}
.service.photo-right .service-photo{right:0}
.service-info{position:absolute;top:0;width:400px;white-space:nowrap}
.service.photo-left .service-info{left:351px;text-align:left}
.service.photo-right .service-info{right:337px;text-align:right}
.service-name{margin-top:22px;font-size:20px;font-weight:300;color:#444}
.service-plan{margin-top:10px;font-size:12px;font-weight:600;letter-spacing:.5px;color:#555}
.service-desc{margin-top:28px;font-size:10.5px;line-height:20px;color:#666}
.call-btn{display:inline-block;margin-top:10px;width:192px;height:28px;line-height:28px;text-align:center;background:var(--green);color:var(--white);font-size:10.5px;font-weight:600;border-radius:2px}

/* orders */
.orders-title{left:0;top:1782px;width:1200px;text-align:center;font-size:19px;font-weight:700;color:#222}
.orders-rule{left:566px;top:1826px;width:55px;height:4px;background:var(--green)}
.register-band{left:202px;top:1877px;width:797px;height:202px;background:linear-gradient(100deg,#4a4a4a 0%,#8f8f8f 40%,#b9b5ae 65%,#5c5c5c 100%)}
.register-label{left:257px;top:1912px;font-size:14px;font-weight:500;color:var(--white)}
.step{width:34px;height:34px;border-radius:50%;background:#1f6fd0;color:var(--white);font-size:13px;font-weight:600;text-align:center;line-height:34px}
.reg-btn{height:38px;line-height:38px;color:var(--white);font-size:13px;font-weight:500;text-align:center;border-radius:2px;white-space:nowrap}
.reg-btn.linkbook{left:254px;top:1992px;width:182px;background:#3b5a9a}
.reg-btn.searchly{left:507px;top:1992px;width:203px;background:var(--red)}
.reg-btn.register{left:785px;top:1976px;width:166px;height:60px;line-height:18px;padding-top:12px;background:var(--red);font-weight:600;text-align:left;padding-left:20px}

/* footer */
.footer-rule{left:0;top:2132px;width:1200px;height:1px;background:var(--line)}
.footer-brand{left:202px;top:2182px;display:flex;align-items:center;gap:8px;color:#444;font-weight:500}
.footer-brand .brand-mark{width:16px;height:20px;background:#444}
.footer-brand .brand-name{font-size:22px}
.footer-brand .brand-sub{font-size:9px}
.footer-col{top:2182px;font-size:11px;color:#444;white-space:nowrap}
.footer-col h4{font-size:11px;font-weight:500;letter-spacing:.5px;margin-bottom:22px}
.footer-col li{list-style:none;line-height:19.5px}
.footer-divider{top:2180px;width:1px;height:110px;background:var(--line)}
.contact dt{font-weight:700}
.contact dd{margin-bottom:18px;line-height:19px;color:#555}
.pay-label{left:528px;top:2347px;font-size:10px;color:#555;letter-spacing:.3px}
.pay-box{left:644px;top:2328px;width:139px;height:41px;border:1px solid #bbb;display:flex;align-items:center;justify-content:center;gap:6px;font-size:13px;font-weight:600;color:var(--blue)}
.pay-box i{width:10px;height:10px;background:var(--blue);display:block}
.copyright{left:0;top:2396px;width:1200px;height:26px;background:var(--footer-band);font-size:8px;color:#666;padding:9px 0 0 202px}
</style>
</head>
<body>

<header>
  <div class="abs brand">
    <span class="brand-mark"></span>
    <div><span class="brand-name">BrightNest</span><span class="brand-sub">by Marguerite</span></div>
  </div>
  <nav class="abs main-nav">
    <a href="#" style="width:89px">Home Page</a>
    <a href="#" style="width:86px">About Us</a>
    <a href="#" class="active" style="width:86px">Services</a>
    <a href="#" style="width:86px">Login</a>
  </nav>
  <div class="abs header-call">Cal Us Now : <span>01555 010 010</span></div>
  <svg class="abs notify" width="26" height="24" viewBox="0 0 26 24" aria-label="Notifications">
    <path d="M2 6h16v10H9l-4 4v-4H2z" fill="#cfcfcf"/>
    <circle cx="19" cy="6" r="5.5" fill="#e53b2c"/>
    <text x="19" y="8.5" font-size="7" fill="#fff" text-anchor="middle" font-family="Montserrat,sans-serif">1</text>
  </svg>
  <div class="abs header-rule"></div>
  <div class="abs breadcrumb">You are here: &nbsp;Home &nbsp;/ &nbsp;Our Services</div>
</header>

<main>
  <div class="abs hero" role="img" aria-label="Hand wiping a wooden table with a yellow cloth beside a fruit bowl"></div>
  <h1 class="abs section-title">WE OFFER THESE CLEANING SERVICES</h1>

  <section class="abs service photo-left" style="top:490px">
    <div class="service-photo" role="img" aria-label="Gloved hands cleaning an oven door" style="background:linear-gradient(110deg,#e07b32 0%,#d9d9d9 45%,#3a3a3a 100%)"></div>
    <div class="service-info">
      <h2 class="service-name">Interior Cleaning</h2>
      <p class="service-plan">FAMILY PACKAGE</p>
      <p class="service-desc">Lorem ipsum dolor sit amet, consectetuer adipiscing elit.<br>Aenean commodo ligula eget dolor.</p>
      <span class="call-btn">Cal Us Now : 01555 010 010</span>
    </div>
  </section>

  <section class="abs service photo-right" style="top:749px">
    <div class="service-photo" role="img" aria-label="Steam iron pressing a shirt" style="background:linear-gradient(120deg,#d8d8dc 0%,#9aa4b8 45%,#3c4460 75%,#c9c6cf 100%)"></div>
    <div class="service-info">
      <h2 class="service-name">Ironing</h2>
      <p class="service-plan">EXTRA CLEAN</p>
      <p class="service-desc">Lorem ipsum dolor sit amet, consectetuer adipiscing elit.<br>Aenean commodo ligula eget dolor.</p>
      <span class="call-btn">Cal Us Now : 01555 010 010</span>
    </div>
  </section>

  <section class="abs service photo-left" style="top:994px">
    <div class="service-photo" role="img" aria-label="Hand cleaning a window with a blue cloth and spray bottle" style="background:linear-gradient(110deg,#9bbd4a 0%,#d7c94a 30%,#3a6fb0 55%,#dcd36a 100%)"></div>
    <div class="service-info">
      <h2 class="service-name">Windows</h2>
      <p class="service-plan">EXPAT SOLO</p>
      <p class="service-desc">Lorem ipsum dolor sit amet, consectetuer adipiscing elit.<br>Aenean commodo ligula eget dolor.</p>
      <span class="call-btn">Cal Us Now : 01555 010 010</span>
    </div>
  </section>

  <section class="abs service photo-right" style="top:1248px">
    <div class="service-photo" role="img" aria-label="Clean wooden deck with railing" style="background:linear-gradient(170deg,#4f6a3a 0%,#8a5a36 35%,#7a5b44 70%,#5e4636 100%)"></div>
    <div class="service-info">
      <h2 class="service-name">Exterior Cleaning</h2>
      <p class="service-plan">EXPAT PRO</p>
      <p class="service-desc">Lorem ipsum dolor sit amet, consectetuer adipiscing elit.<br>Aenean commodo ligula eget dolor.</p>
      <span class="call-btn">Cal Us Now : 01555 010 010</span>
    </div>
  </section>

  <section class="abs service photo-left" style="top:1508px">
    <div class="service-photo" role="img" aria-label="Brush cleaning a suit jacket" style="background:linear-gradient(110deg,#2a2624 0%,#5a4a40 45%,#3d3430 75%,#1e1b1a 100%)"></div>
    <div class="service-info">
      <h2 class="service-name">Dry Cleaning</h2>
      <p class="service-plan">CREATE YOUR OWN</p>
      <p class="service-desc">Lorem ipsum dolor sit amet, consectetuer adipiscing elit.<br>Aenean commodo ligula eget dolor.</p>
      <span class="call-btn">Cal Us Now : 01555 010 010</span>
    </div>
  </section>

  <h2 class="abs orders-title">Awaiting Your Orders</h2>
  <div class="abs orders-rule"></div>

  <div class="abs register-band" role="img" aria-label="Hand cleaning a stainless steel gas hob with a blue sponge"></div>
  <div class="abs register-label">Simple Registration</div>
  <div class="abs step" style="left:257px;top:1947px">1</div>
  <div class="abs step" style="left:514px;top:1947px">2</div>
  <div class="abs step" style="left:788px;top:1947px">3</div>
  <div class="abs reg-btn linkbook">Login with Linkbook</div>
  <div class="abs reg-btn searchly">Sign in with Searchly</div>
  <div class="abs reg-btn register">REGISTER<br>NOW</div>
</main>

<footer>
  <div class="abs footer-rule"></div>
  <div class="abs footer-brand">
    <span class="brand-mark"></span>
    <div><span class="brand-name">BrightNest</span><span class="brand-sub">by Marguerite</span></div>
  </div>

  <div class="abs footer-col" style="left:533px">
    <h4>NAVIGATION</h4>
    <ul><li>Home Page</li><li>About Us</li><li>Services</li><li>Login</li></ul>
  </div>
  <div class="abs footer-divider" style="left:643px"></div>
  <div class="abs footer-col" style="left:686px">
    <h4>FOLLOW US</h4>
    <ul><li>Linkbook</li><li>Chirper</li><li>Searchly Plus</li><li>RSS</li></ul>
  </div>
  <div class="abs footer-divider" style="left:780px"></div>
  <div class="abs footer-col contact" style="left:814px">
    <h4>CONTACT US</h4>
    <dl>
      <dt>Telephone:</dt><dd>Number &nbsp;01555 010 010</dd>
      <dt>Email Address:</dt><dd>info@brightnest.example</dd>
      <dt>Offices:</dt><dd>Registered Office: 24<br>Meadow Lane, Ashby, AB1 2CD</dd>
    </dl>
  </div>

  <div class="abs pay-label">PAYMENT OPTIONS</div>
  <div class="abs pay-box"><i></i>Paymora</div>

  <div class="abs copyright">© 2017 BrightNest Services Limited. All rights reserved.</div>
</footer>

</body>
</html>
```